Business Card Design Project

We need a simple business card design that uses our current logo.
We need to have the current logo put into a high res format.
We need to have 1 card made with contact information.
We will supply the information for the 4 employees.
Industry/Entity Type
Business
Requirements
Must have
- The contact information is as follows:
Mark Dellweather
Producer/CEO
c. 410-555-0147
f. 410-555-0193
markd@lanternbay.example
Al Vostrand, CFO
c. 949-555-0162
f. 410-555-0193
alv@lanternbay.example
Peter Malvane, PR
c. 267-555-0128
f. 410-555-0193
pmalvane@lanternbay.example
Tim Garrowby, Producer
c. 949-555-0184
f. 410-555-0193
timg@lanternbay.example
The address for all cards is:
318 W Calle Norvento #2715, Marrow Cove, WA 92681

```html
<!DOCTYPE html>
<html lang="en">
<head>
<meta charset="utf-8">
<title>Lantern Bay Media – Business Card</title>
<link rel="stylesheet" href="https://fonts.googleapis.com/css2?family=Arimo:wght@400;700&display=swap">
<style>
  :root {
    --stage-bg: #d9d9d9;
    --card-white: #fbfbfb;
    --sky-light: #b9e3f5;
    --sky-deep: #3fa9e6;
    --ink: #1f1f1f;
    --ink-soft: #333333;
    --accent: #3aa6e0;
    --icon-fg: #ffffff;
  }
  * { box-sizing: border-box; margin: 0; padding: 0; }
  html, body { width: 1200px; height: 900px; overflow: hidden; }
  body {
    background: var(--stage-bg);
    font-family: "Arimo", Arial, sans-serif;
    color: var(--ink);
    display: flex;
    flex-direction: column;
    align-items: center;
    justify-content: center;
    gap: 48px;
  }
  .card {
    width: 620px;
    height: 354px;
    position: relative;
    box-shadow: 0 6px 18px rgba(0,0,0,0.18);
  }
  .card-back {
    background: linear-gradient(180deg, var(--sky-light) 0%, var(--sky-deep) 100%);
    display: flex;
    align-items: center;
    justify-content: center;
  }
  .brand-name {
    font-family: "Arimo", Arial, sans-serif;
    font-weight: 700;
    text-transform: uppercase;
    letter-spacing: 1px;
    white-space: nowrap;
  }
  .card-back .brand-name { font-size: 50px; color: var(--ink); }
  .card-front { background: var(--card-white); padding: 30px 34px; }
  .card-front .brand-name { font-size: 44px; color: var(--accent); }
  .holder {
    position: absolute;
    left: 34px;
    top: 166px;
  }
  .holder-name { font-size: 25px; font-weight: 400; text-transform: uppercase; color: var(--ink); }
  .holder-title { font-size: 17px; color: var(--ink-soft); margin-top: 2px; }
  .contact-list {
    position: absolute;
    left: 318px;
    top: 176px;
    list-style: none;
  }
  .contact-item {
    display: flex;
    align-items: flex-start;
    gap: 12px;
    font-size: 17px;
    line-height: 20px;
    color: var(--ink);
    margin-bottom: 11px;
  }
  .contact-icon {
    flex: none;
    width: 22px;
    height: 22px;
    border-radius: 50%;
    background: var(--accent);
    display: flex;
    align-items: center;
    justify-content: center;
  }
  .contact-icon svg { width: 13px; height: 13px; fill: var(--icon-fg); }
</style>
</head>
<body>

  <section class="card card-back" aria-label="Business card back">
    <span class="brand-name">Lantern Bay Media</span>
  </section>

  <section class="card card-front" aria-label="Business card front">
    <span class="brand-name">Lantern Bay Media</span>

    <div class="holder">
      <p class="holder-name">Mark Dellweather</p>
      <p class="holder-title">Producer/CEO</p>
    </div>

    <ul class="contact-list">
      <li class="contact-item">
        <span class="contact-icon" aria-hidden="true">
          <svg viewBox="0 0 16 16"><path d="M3.5 1.5l2.3 2.6-1.3 1.6c.9 2 2.5 3.6 4.5 4.6l1.6-1.3 2.6 2.3-1.4 2.2C6.6 13.3 2.7 9.4 1.4 4.2z"/></svg>
        </span>
        <span>410-555-0147</span>
      </li>
      <li class="contact-item">
        <span class="contact-icon" aria-hidden="true">
          <svg viewBox="0 0 16 16"><rect x="4" y="1.5" width="8" height="4"/><rect x="1.5" y="6" width="13" height="6" rx="1"/><rect x="4" y="10" width="8" height="4.5" fill="#3aa6e0" stroke="#fff" stroke-width="1"/></svg>
        </span>
        <span>410-555-0193</span>
      </li>
      <li class="contact-item">
        <span class="contact-icon" aria-hidden="true">
          <svg viewBox="0 0 16 16"><path d="M1.5 3.5h13v9h-13z M2.5 4.5l5.5 4.5 5.5-4.5" fill="none" stroke="#fff" stroke-width="1.4"/></svg>
        </span>
        <span>markd@lanternbay.example</span>
      </li>
      <li class="contact-item">
        <span class="contact-icon" aria-hidden="true">
          <svg viewBox="0 0 16 16"><path d="M8 1a5 5 0 0 0-5 5c0 3.6 5 9 5 9s5-5.4 5-9a5 5 0 0 0-5-5zm0 7a2 2 0 1 1 0-4 2 2 0 0 1 0 4z"/></svg>
        </span>
        <span>318 W Calle Norvento #2715,<br>Marrow Cove, WA 92681</span>
      </li>
    </ul>
  </section>

</body>
</html>
```